Valentine's Day Flyer

We require an A5 size flyer to promote our February parking offer & Giveaway.

Offer:
Book your parking online & Save!
$5 Night/Weekend Parking
$10 Early Bird Parking

Giveaway: Win a $5,000 Diamond Ring!
Every time you book your parking online using Trundle-Nook you get a chance to win!

The final design should contain:
- Valentine's Theme
- Emphasise 'Book your parking online & Save!'

Designers: please visit www.halvorbaypark.com.au for more info on Halvor Bay Parking & Trundle-Nook

Target Market(s)

18-50 year old drivers

Industry/Entity Type

Parking

```html
<!DOCTYPE html>
<html lang="en">
<head>
<meta charset="utf-8">
<title>Halvor Bay Parking – Valentine's Offer</title>
<link rel="stylesheet" href="https://fonts.googleapis.com/css2?family=Anton&display=swap">
<style>
  :root {
    --magenta: #d0097f;
    --magenta-deep: #c2057a;
    --blue: #0b91d2;
    --blue-deep: #0a5fa8;
    --pink-light: #f6b9d6;
    --pink-mid: #ef8fbf;
    --white: #ffffff;
    --ink: #2f2f2f;
    --ink-soft: #3a3a3a;
    --steel-light: #d2d3d5;
    --steel-dark: #9c9ea1;
    --frame: #3b3b3b;
  }
  html, body {
    margin: 0;
    padding: 0;
    width: 846px;
    height: 1200px;
    overflow: hidden;
    background: var(--magenta);
  }
  .flyer {
    position: relative;
    width: 846px;
    height: 1200px;
    overflow: hidden;
    background: radial-gradient(circle at 50% 45%, var(--magenta) 0%, var(--magenta-deep) 100%);
    font-family: "Anton", "Impact", sans-serif;
  }
  .headline span {
    position: absolute;
    line-height: 1;
    white-space: nowrap;
    transform: scaleY(1.12);
    transform-origin: top left;
  }
  .headline .book { left: 166px; top: 58px; font-size: 70px; color: var(--white); }
  .headline .parking { left: 242px; top: 128px; font-size: 108px; color: var(--blue); }
  .headline .online { left: 272px; top: 240px; font-size: 60px; color: var(--white); }
  .headline .save { left: 484px; top: 232px; font-size: 110px; color: var(--blue); }

  .lock-panel {
    position: absolute;
    left: 179px;
    top: 371px;
    width: 472px;
    height: 472px;
    border: 5px solid var(--frame);
    border-radius: 38px;
    background: linear-gradient(135deg, var(--steel-light) 0%, var(--steel-dark) 100%);
    box-shadow: 0 6px 14px rgba(0,0,0,0.35);
  }

  .heart {
    position: absolute;
  }
  .heart svg {
    position: absolute;
    inset: 0;
    width: 100%;
    height: 100%;
    overflow: visible;
  }
  .heart .shape { stroke: var(--white); stroke-width: 2.5; }
  .heart .label {
    position: absolute;
    inset: 0;
    display: flex;
    flex-direction: column;
    align-items: center;
    text-align: center;
    line-height: 1;
  }
  .price { display: flex; align-items: flex-start; }
  .price .cents { font-size: 0.5em; margin-top: 0.08em; }
  .caption { font-size: 15px; line-height: 1.05; }

  .heart-night { left: 46px; top: 290px; width: 222px; height: 220px; transform: rotate(-8deg); }
  .heart-night .shape { fill: var(--pink-light); }
  .heart-night .label { color: var(--ink); padding-top: 58px; transform: rotate(-12deg); }
  .heart-night .price { font-size: 76px; }

  .heart-early { left: 18px; top: 522px; width: 226px; height: 220px; transform: rotate(10deg); }
  .heart-early .shape { fill: var(--blue); }
  .heart-early .label { color: var(--pink-light); padding-top: 56px; transform: rotate(6deg); }
  .heart-early .price { font-size: 76px; }

  .heart-ring { left: 616px; top: 740px; width: 122px; height: 114px; }
  .heart-ring .shape { fill: var(--pink-mid); }

  .heart-win { left: 518px; top: 800px; width: 220px; height: 206px; }
  .heart-win .shape { fill: var(--pink-light); }
  .heart-win .label { color: var(--ink-soft); align-items: flex-start; padding: 40px 0 0 24px; text-align: left; }
  .win-line { display: flex; align-items: flex-start; }
  .win-line .big { font-size: 52px; }
  .win-line .a { font-size: 26px; margin-top: 2px; }
  .win-amount { font-size: 32px; margin: -24px 0 0 76px; }
  .win-prize { font-size: 24px; margin-left: 56px; line-height: 1.05; text-align: center; }

  .heart-chance { left: 668px; top: 914px; width: 158px; height: 146px; }
  .heart-chance .shape { fill: var(--pink-light); }
  .heart-chance .label { color: var(--ink-soft); font-size: 11.5px; line-height: 1.15; padding: 36px 16px 0; }

  .brand {
    position: absolute;
    left: 181px;
    top: 1056px;
    width: 484px;
    height: 91px;
    display: flex;
    align-items: center;
    justify-content: center;
    gap: 18px;
    background: var(--blue);
  }
  .brand .mark {
    width: 34px;
    height: 34px;
    background: var(--white);
  }
  .brand .name {
    color: var(--white);
    font-size: 48px;
    line-height: 1;
  }
</style>
</head>
<body>
<main class="flyer" role="img" aria-label="Magenta background scattered with a pattern of soft pink hearts">
  <h1 class="headline">
    <span class="book">Book your</span>
    <span class="parking">parking</span>
    <span class="online">online &amp;</span>
    <span class="save">Save!</span>
  </h1>

  <div class="lock-panel" role="img" aria-label="Silver rounded square icon showing a car with a padlock body, over a faint heart pattern"></div>

  <div class="heart heart-night">
    <svg viewBox="0 0 100 90" aria-hidden="true"><path class="shape" d="M50 88 C20 65 2 48 2 27 C2 12 14 2 27 2 C38 2 46 9 50 17 C54 9 62 2 73 2 C86 2 98 12 98 27 C98 48 80 65 50 88Z"/></svg>
    <div class="label">
      <div class="price"><span>$5</span><span class="cents">00</span></div>
      <div class="caption">Night/Weekend<br>Parking</div>
    </div>
  </div>

  <div class="heart heart-early">
    <svg viewBox="0 0 100 90" aria-hidden="true"><path class="shape" d="M50 88 C20 65 2 48 2 27 C2 12 14 2 27 2 C38 2 46 9 50 17 C54 9 62 2 73 2 C86 2 98 12 98 27 C98 48 80 65 50 88Z"/></svg>
    <div class="label">
      <div class="price"><span>$10</span><span class="cents">00</span></div>
      <div class="caption">Early Bird<br>Parking</div>
    </div>
  </div>

  <div class="heart heart-ring" role="img" aria-label="Diamond ring icon">
    <svg viewBox="0 0 100 90" aria-hidden="true"><path class="shape" d="M50 88 C20 65 2 48 2 27 C2 12 14 2 27 2 C38 2 46 9 50 17 C54 9 62 2 73 2 C86 2 98 12 98 27 C98 48 80 65 50 88Z"/></svg>
  </div>

  <div class="heart heart-win">
    <svg viewBox="0 0 100 90" aria-hidden="true"><path class="shape" d="M50 88 C20 65 2 48 2 27 C2 12 14 2 27 2 C38 2 46 9 50 17 C54 9 62 2 73 2 C86 2 98 12 98 27 C98 48 80 65 50 88Z"/></svg>
    <div class="label">
      <div class="win-line"><span class="big">WIN</span><span class="a">a</span></div>
      <div class="win-amount">$5,000</div>
      <div class="win-prize">Diamond<br>Ring!</div>
    </div>
  </div>

  <div class="heart heart-chance">
    <svg viewBox="0 0 100 90" aria-hidden="true"><path class="shape" d="M50 88 C20 65 2 48 2 27 C2 12 14 2 27 2 C38 2 46 9 50 17 C54 9 62 2 73 2 C86 2 98 12 98 27 C98 48 80 65 50 88Z"/></svg>
    <p class="label">Every time you book your parking online using Trundle-Nook you get a chance to win!</p>
  </div>

  <footer class="brand">
    <span class="mark" aria-hidden="true"></span>
    <span class="name">Halvor Bay Parking</span>
  </footer>
</main>
</body>
</html>
```